Business cards in digital learning for freelancer

Hello, I need a business cards in french. I work in the Digital learning industries as freeelancer; I'm an expert in digital learning. I work in France. My customer are in the health industry, pharmaceutical industry, and training organization. I've got a logo. I offer three services: consulting, Design, and Training. In the consulting, I offers coaching to choose your digital learning tools and the digital learning strategy. For the Design, I product differents level of elearning like rapid-learning, elearning, micro-learning, video-learning. And for the training service, I've create training about pedagogy, digital learning management project, Digital learning design.
I join my Logo create in this platform. My universe is gamified. I like the life, and I'm very social. I want a card like I'm I. I love Art (painting), Europeen comics. I use in my visual support "permanent maker" font and caracters. I would like cards: elegant, modern, Top class. If you need any information, you can ask me.
thanks for ideas

Target Market(s)

in health industries and training organization for Training manager, instructor, human resources director

Contact Information for Business Card

Phone number : 06 31 87 59 14 , mail: lucienmorvaltes@courriel-nord.fr, web: lucienmorvaltes.fr , LinkedIn

Font styles to use
Sans Serif

Requirements
Must have
• Use my logo and write my 3 services (consulting, training, design)

```html
<!DOCTYPE html>
<html lang="fr">
<head>
<meta charset="utf-8">
<title>Lucien Morvaltes — Cartes de visite</title>
<link rel="stylesheet" href="https://fonts.googleapis.com/css2?family=Jost:wght@400;500;600&family=Cinzel:wght@400&display=swap">
<style>
  :root {
    --backdrop: #e6e6e4;
    --card-white: #f7f7f5;
    --brand-orange: #d9662a;
    --ink-grey: #6b6b6b;
    --rule-grey: #8a8a8a;
    --paper-white: #fbf7f3;
  }
  * { box-sizing: border-box; margin: 0; padding: 0; }
  html, body { width: 1200px; height: 801px; overflow: hidden; }
  body {
    background: var(--backdrop);
    font-family: "Jost", sans-serif;
    position: relative;
  }
  .card {
    position: absolute;
    top: 246px;
    width: 540px;
    height: 309px;
    box-shadow: 0 10px 28px rgba(0,0,0,.14);
  }
  .card--front { left: 40px; background: var(--card-white); }
  .card--back  { left: 620px; background: var(--brand-orange); }

  /* front */
  .brand-lockup {
    position: absolute;
    right: 34px;
    top: 60px;
    display: flex;
    flex-direction: column;
    align-items: flex-end;
  }
  .brand-mark-row { display: flex; align-items: center; gap: 12px; }
  .brand-dot {
    width: 34px; height: 34px; border-radius: 50%;
    background: var(--brand-orange);
  }
  .brand-name {
    font-family: "Jost", sans-serif;
    font-weight: 600;
    font-size: 38px;
    letter-spacing: 1px;
    color: var(--brand-orange);
    line-height: 1;
  }
  .brand-tagline {
    font-family: "Cinzel", serif;
    font-size: 12px;
    letter-spacing: 1.5px;
    color: var(--ink-grey);
    margin-top: 8px;
  }
  .front-rule {
    position: absolute;
    left: 210px;
    right: 34px;
    top: 172px;
    height: 1px;
    background: var(--rule-grey);
  }
  .holder {
    position: absolute;
    left: 34px;
    top: 152px;
  }
  .holder-name {
    font-size: 20px;
    font-weight: 500;
    color: var(--brand-orange);
    line-height: 1.1;
  }
  .holder-role {
    font-size: 14px;
    color: var(--ink-grey);
    margin-top: 2px;
  }
  .contact-list {
    position: absolute;
    left: 34px;
    top: 214px;
    list-style: none;
  }
  .contact-item {
    display: flex;
    align-items: center;
    gap: 8px;
    font-size: 12.5px;
    color: var(--ink-grey);
    line-height: 19px;
  }
  .contact-icon { width: 13px; height: 13px; flex: none; }

  /* back */
  .back-lockup {
    position: absolute;
    inset: 0;
    display: flex;
    flex-direction: column;
    align-items: center;
    justify-content: center;
    gap: 12px;
  }
  .back-lockup .brand-dot { background: var(--paper-white); width: 40px; height: 40px; }
  .back-lockup .brand-name { color: var(--paper-white); font-size: 46px; }
  .back-lockup .brand-tagline { color: var(--paper-white); font-size: 15px; margin-top: 0; }
</style>
</head>
<body>

<section class="card card--front" aria-label="Recto de la carte">
  <div class="brand-lockup">
    <div class="brand-mark-row">
      <span class="brand-dot"></span>
      <span class="brand-name">MORVALTES</span>
    </div>
    <span class="brand-tagline">Digital Learning</span>
  </div>
  <div class="front-rule"></div>

  <div class="holder">
    <p class="holder-name">Lucien Morvaltes</p>
    <p class="holder-role">Digital Learning consultant</p>
  </div>

  <ul class="contact-list">
    <li class="contact-item">
      <svg class="contact-icon" viewBox="0 0 14 14"><circle cx="7" cy="7" r="7" fill="#d9662a"/><path d="M4.3 4.2c.3-.3.8-.3 1 0l.8 1c.2.3.2.6 0 .8l-.4.4c.4.8 1 1.4 1.8 1.8l.4-.4c.2-.2.5-.2.8 0l1 .8c.3.2.3.7 0 1l-.5.5c-2.4.3-5.3-2.6-5.3-5.3z" fill="#fff"/></svg>
      06 31 87 59 14
    </li>
    <li class="contact-item">
      <svg class="contact-icon" viewBox="0 0 14 14"><circle cx="7" cy="7" r="7" fill="#d9662a"/><rect x="3.5" y="4.5" width="7" height="5" fill="none" stroke="#fff" stroke-width="1"/><path d="M3.5 4.5 7 7.3l3.5-2.8" fill="none" stroke="#fff" stroke-width="1"/></svg>
      lucienmorvaltes@courriel-nord.fr
    </li>
    <li class="contact-item">
      <svg class="contact-icon" viewBox="0 0 14 14"><circle cx="7" cy="7" r="7" fill="#d9662a"/><circle cx="7" cy="7" r="3.6" fill="none" stroke="#fff" stroke-width="1"/><path d="M3.4 7h7.2M7 3.4c-1.6 2-1.6 5.2 0 7.2M7 3.4c1.6 2 1.6 5.2 0 7.2" fill="none" stroke="#fff" stroke-width=".8"/></svg>
      lucienmorvaltes.fr
    </li>
    <li class="contact-item">
      <svg class="contact-icon" viewBox="0 0 14 14"><circle cx="7" cy="7" r="7" fill="#d9662a"/></svg>
      /in/lucien-morvaltes-elearning
    </li>
  </ul>
</section>

<section class="card card--back" aria-label="Verso de la carte">
  <div class="back-lockup">
    <div class="brand-mark-row">
      <span class="brand-dot"></span>
      <span class="brand-name">MORVALTES</span>
    </div>
    <span class="brand-tagline">Consulting, Training, Design</span>
  </div>
</section>

</body>
</html>
```